Global social media analytics company needs business card design

We need an updated business card design to align with our new website - brightquillo.net -

I would also like a favicon designed as well.

Target Market(s)

CEOs, CMOs go big companies

Industry/Entity Type

Business

Contact Information for Business Card

Room for the following:
Address
Main telephone
Direct telephone or cell phone
twitter handle

Colors
aaaaaa

Requirements
Must have
• Attention to detail; style.
• Use the logo color from our website - which is gray

```html
<!DOCTYPE html>
<html lang="en">
<head>
<meta charset="utf-8">
<title>Brightquillo Business Card</title>
<link href="https://fonts.googleapis.com/css2?family=Arimo:wght@400;700&display=swap" rel="stylesheet">
<style>
  :root {
    --backdrop: #e8e5e1;
    --card-white: #ffffff;
    --brand-gray: #aaaaaa;
    --wave-dark: #5f5f61;
    --text-strong: #222222;
    --text-company: #575757;
    --text-address: #666666;
    --accent-blue: #3fa9e0;
  }
  * { box-sizing: border-box; margin: 0; padding: 0; }
  html, body {
    width: 1173px; height: 1200px; overflow: hidden;
    background: var(--backdrop);
    font-family: "Arimo", Arial, sans-serif;
  }
  .card {
    position: absolute;
    width: 877px; height: 500px;
    overflow: hidden;
  }
  .card-front {
    left: 134px; top: 73px;
    background: var(--card-white);
    border: 1px solid #8c8c8c;
  }
  .card-back {
    left: 132px; top: 616px;
    background: var(--brand-gray);
  }
  .wave { position: absolute; inset: 0; width: 100%; height: 100%; }
  .brand {
    position: absolute; left: 41px; top: 28px;
    display: flex; align-items: center; gap: 20px;
  }
  .brand-dot {
    width: 126px; height: 126px; border-radius: 50%;
    background: var(--brand-gray);
  }
  .brand-name {
    font-size: 52px; font-weight: 700; color: var(--brand-gray);
    letter-spacing: -0.5px;
  }
  .company {
    position: absolute; left: 41px; top: 240px;
    color: var(--text-company);
  }
  .company-name { font-size: 20px; font-weight: 700; letter-spacing: 0.3px; margin-bottom: 6px; }
  .company-address { font-size: 22px; line-height: 29px; color: var(--text-address); }
  .contacts {
    position: absolute; right: 36px; top: 323px;
    list-style: none; text-align: right;
    font-size: 22px; color: var(--text-strong);
  }
  .contacts li {
    height: 41.5px; display: flex; justify-content: flex-end; align-items: center; gap: 10px;
  }
  .contacts svg { width: 20px; height: 20px; fill: var(--text-strong); }
  .contacts .handle-dot { width: 18px; height: 18px; border-radius: 50%; background: var(--accent-blue); }
  .holder {
    position: absolute; left: 41px; top: 452px;
    font-size: 20px; color: var(--text-strong);
  }
  .holder-name { font-size: 28px; font-weight: 700; }
  .back-mark {
    position: absolute; left: 263px; top: 75px;
    width: 350px; height: 350px; border-radius: 50%;
    background: var(--card-white);
  }
</style>
</head>
<body>
  <section class="card card-front">
    <svg class="wave" viewBox="0 0 1050 598" preserveAspectRatio="none" aria-hidden="true">
      <path fill="var(--brand-gray)" d="M0 478 C150 530 320 500 520 435 C720 372 900 336 1050 345 L1050 598 L0 598 Z"/>
      <path fill="var(--wave-dark)" d="M0 418 C130 472 310 468 520 398 C700 342 880 314 1050 320 L1050 328 C880 326 700 362 520 420 C320 488 130 500 0 458 Z"/>
    </svg>

    <div class="brand">
      <span class="brand-dot"></span>
      <span class="brand-name">brightquillo</span>
    </div>

    <div class="company">
      <p class="company-name">BRIGHTQUILLO, INC.</p>
      <p class="company-address">2218 Harwell Ave. 4th Fl<br>Fairmont, MA 02190, USA</p>
    </div>

    <ul class="contacts">
      <li>
        <svg viewBox="0 0 24 24" aria-hidden="true"><path d="M12 1a11 11 0 1 0 0 22 11 11 0 0 0 0-22zm0 2a9 9 0 1 1 0 18 9 9 0 0 1 0-18zm-3 3c-1 0-2 1-2 3 0 5 4 9 8 9 2 0 3-1 3-2l-2-2-2 1c-2-1-3-2-4-4l1-2z"/></svg>
        <span>+1 555 310 4427</span>
      </li>
      <li>
        <svg viewBox="0 0 24 24" aria-hidden="true"><path d="M9 0h2v4h4a2 2 0 0 1 2 2v16a2 2 0 0 1-2 2H7a2 2 0 0 1-2-2V6a2 2 0 0 1 2-2h2zM8 7v5h8V7zm0 7v2h2v-2zm3 0v2h2v-2zm3 0v2h2v-2zm-6 3v2h2v-2zm3 0v2h2v-2zm3 0v2h2v-2z"/></svg>
        <span>+123 456 7890</span>
      </li>
      <li>
        <svg viewBox="0 0 24 24" aria-hidden="true"><path d="M1 5h22v2l-11 7L1 7zm0 4l11 7 11-7v10H1z"/></svg>
        <span>info@brightquillo.net</span>
      </li>
      <li>
        <span class="handle-dot"></span>
        <span>@brightquillo</span>
      </li>
    </ul>

    <p class="holder"><span class="holder-name">Your Name,</span> Title</p>
  </section>

  <section class="card card-back">
    <span class="back-mark"></span>
  </section>
</body>
</html>
```